Business Card Design

chiropractor. Searching for a fresh cool look. Tired of all the run of the mill designs. I am open tocolors and all new designs..

Target Market(s)

auto accidents workers compensation and private insurance

Industry/Entity Type

Business

Contact Information for Business Card

Dr. Mark S. Snyder193-02 northern blvd.Flushing, new york 11358Upper level rear suitephone 718 224 3605fax 718 555 0187

Font styles to use
Sans Serif

Requirements
Must have
• my office hours on back of card
• monday 9am-noon; 2:30pm-7pm
• tuesday 2:30pm-7pm
• wednesday 9am-noon; 2;30pm-7pm
• thursday 4pm-7pm
• friday4pm-7pm
Nice to have
• some kind of real cool logo

```html
<!DOCTYPE html>
<html lang="en">
<head>
<meta charset="utf-8">
<title>Business Card – Dr. Paul T. Wexley</title>
<link href="https://fonts.googleapis.com/css2?family=Montserrat:wght@500;600&display=swap" rel="stylesheet">
<style>
  :root {
    --backdrop: #cfd3dc;
    --card: #ffffff;
    --ink: #111111;
    --sage: #9bbd8a;
  }
  * { margin: 0; padding: 0; box-sizing: border-box; }
  html, body {
    width: 1200px;
    height: 347px;
    overflow: hidden;
  }
  body {
    position: relative;
    background: var(--backdrop);
    font-family: "Montserrat", sans-serif;
    color: var(--ink);
  }
  .card {
    position: absolute;
    top: 20px;
    width: 542px;
    height: 307px;
    background: var(--card);
  }
  .card--back { left: 25px; }
  .card--front { left: 628px; }

  .hours {
    position: absolute;
    left: 68px;
    top: 64px;
    font-weight: 600;
    font-size: 19.5px;
    line-height: 28px;
  }
  .hours__title {
    font-size: inherit;
    font-weight: 600;
  }
  .hours__list { list-style: none; }

  .brand {
    position: absolute;
    left: 0;
    right: 0;
    top: 84px;
    display: flex;
    justify-content: center;
    align-items: center;
    gap: 10px;
    color: var(--sage);
    font-weight: 600;
    font-size: 24px;
  }
  .brand__dot {
    width: 14px;
    height: 14px;
    border-radius: 50%;
    background: var(--sage);
  }
  .doctor-name {
    position: absolute;
    left: 0;
    right: 0;
    top: 150px;
    text-align: center;
    font-weight: 600;
    font-size: 22px;
  }
  .contact {
    position: absolute;
    left: 89px;
    top: 228px;
    font-style: normal;
    font-weight: 600;
    font-size: 15.5px;
    line-height: 20px;
  }
</style>
</head>
<body>
  <section class="card card--back" aria-label="Card back: office hours">
    <div class="hours">
      <h2 class="hours__title">Office Hours</h2>
      <ul class="hours__list">
        <li>Monday - 8am-11am / 3pm-6:30pm</li>
        <li>Tuesday - 1:30pm-6pm</li>
        <li>Wednesday - 8am-11am / 1:30pm-6:30pm</li>
        <li>Thursday - 3pm-8pm</li>
        <li>Friday - 10am-2pm</li>
      </ul>
    </div>
  </section>

  <section class="card card--front" aria-label="Card front: contact details">
    <div class="brand">
      <span class="brand__dot"></span>
      <span class="brand__name">Wexley Chiropractic</span>
    </div>
    <h1 class="doctor-name">Dr. Paul T. Wexley</h1>
    <address class="contact">
      287-14 Hollis Ridge rd. Corwin Heights, NY<br>
      11472 Second Floor Suite B<br>
      p.718.555.0142 / f. 718.555.0187
    </address>
  </section>
</body>
</html>
```